Criminal Defense Law Firm needs Stationary design Theme for a Business Card, Envelope, and Letterhea

Our Law Firm is seeking a general design concept for a business card, letterhead, and Envelope.

Our website is QuillmoreAdvocates.com

A design for these three items is requested to keep branding in place for the firm. Would like to keep the Firm Colors on the website consistent with our branding on business cards, letterheads, and mailing envelopes #10 size to be exact.

We would like business cards printed front and back with Law firm Colors from website.

Letterhead with law firm colors as well. Design is not limited to just the header, but the footer can be utilized as well for email, website, phone, fax, etc.

Simple #10 envelope consisting of the same design principles set out in the previous two designs.

```html
<!DOCTYPE html>
<html lang="en">
<head>
<meta charset="utf-8">
<title>Quillmore Criminal Law Offices — #10 Envelope</title>
<link rel="stylesheet" href="https://fonts.googleapis.com/css2?family=Cormorant+Garamond:wght@500&family=Open+Sans:wght@400&display=swap">
<style>
  :root {
    --backdrop: #c4c4c4;
    --paper: #ffffff;
    --paper-shade: #f1f1f1;
    --ink: #1f1d1d;
    --flap: #1e1c1b;
    --gold: #a08a5c;
    --window: #e9eaec;
    --window-edge: #d6d7da;
  }
  * { box-sizing: border-box; margin: 0; padding: 0; }
  html, body {
    width: 1200px; height: 795px; overflow: hidden;
    background: var(--backdrop);
  }
  .canvas { position: relative; width: 1200px; height: 795px; }

  .envelope {
    position: absolute;
    width: 560px; height: 244px;
    background: linear-gradient(180deg, var(--paper), var(--paper-shade));
    box-shadow: 0 6px 14px rgba(0,0,0,0.12);
  }

  /* Back of envelope */
  .envelope--back { left: 70px; top: 130px; }
  .envelope__flap {
    position: absolute; left: 0; top: 0;
    width: 100%; height: 104px;
    background: var(--flap);
    border-radius: 0 0 14px 14px;
    display: flex; align-items: center; justify-content: center; gap: 10px;
  }
  .flap-mark__dot {
    width: 22px; height: 22px; border-radius: 50%;
    border: 1.5px solid var(--gold);
  }
  .flap-mark__name {
    font-family: "Cormorant Garamond", serif;
    font-weight: 500; font-size: 20px; letter-spacing: 3px;
    color: var(--gold); text-transform: uppercase;
  }

  /* Front of envelope */
  .envelope--front { left: 570px; top: 420px; }
  .return-address {
    position: absolute; left: 26px; top: 26px;
    display: flex; align-items: flex-start; gap: 10px;
  }
  .return-address__dot {
    width: 24px; height: 24px; border-radius: 50%;
    border: 1.3px solid var(--ink); margin-top: 2px;
  }
  .return-address__name {
    font-family: "Cormorant Garamond", serif;
    font-weight: 500; font-size: 12.5px; line-height: 1.1;
    letter-spacing: 1px; color: var(--ink); text-transform: uppercase;
  }
  .return-address__street {
    margin-top: 6px; padding-left: 7px;
    border-left: 1px solid var(--gold);
    font-family: "Open Sans", sans-serif;
    font-size: 7px; line-height: 1.5; color: var(--ink);
  }
  .envelope__window {
    position: absolute; right: 30px; top: 110px;
    width: 210px; height: 90px;
    background: linear-gradient(160deg, var(--window), #f6f6f7 55%, var(--window));
    border: 1px solid var(--window-edge);
    border-radius: 10px;
  }
</style>
</head>
<body>
<main class="canvas">
  <section class="envelope envelope--back" aria-label="Envelope back">
    <div class="envelope__flap">
      <span class="flap-mark__dot"></span>
      <span class="flap-mark__name">Quillmore</span>
    </div>
  </section>

  <section class="envelope envelope--front" aria-label="Envelope front">
    <div class="return-address">
      <span class="return-address__dot"></span>
      <div>
        <p class="return-address__name">Quillmore Criminal<br>Law Offices</p>
        <p class="return-address__street">214 Harlow Avenue SW<br>Fairbrook, NM 87190</p>
      </div>
    </div>
    <div class="envelope__window"></div>
  </section>
</main>
</body>
</html>
```